Aircraft maintenance buisness card

I am an aircraft mechanic looking for a personal buisness card . I would like my name and a title of Aircraft Maintenance Manager . I would like a suttle picture of an aircraft and helicopter .

elegant and professional wtih my contact .

My name should be on the car and Aircraft Maintenance Manager under with my contact infor below .

i have attached some pictures but i am open to other pics and ideas . I would like a airliner or private jet and a helicopter in the picture . The Images should be suttle and not the main idea . I also uploaded a picture of a jet engine which is cool . Be creative and i will work with you to finalize something .
Updates

Project Deadline Extended
Reason: Looking for more variations . Very good so far but looiking for a bit more styles and i uploaded my logo that i purchased . Please use my logo and be creative with it . I like some variations of black card with maybe some pictures that i uploaded but i am open to ideas . Be creative and i will work with you .

Project Deadline Extended
Reason: Looking for more designs and variations . Not yet satisfied with the designs i have gotten .

Industry/Entity Type

Aviation

Contact Information for Business Card

Aircraft Maintenance Manager

Font styles to use
Serif

Colors

Designer to choose colors to be used in the design.

Requirements
Must have
• An aviation related Logo if possible incorporated in the card possibly
• My name
• Tiberio Malvade Furtunato
• 482 Pellow St.
• Halvick , OR
• 08519
• Email: Lwskyfixtech@mailvora.com
Nice to have
• Suttle Backround of a Private Jet or Airliner and a Helicopter .

```html
<!DOCTYPE html>
<html lang="en">
<head>
<meta charset="utf-8">
<title>Veltra Aviation – Business Card</title>
<link rel="stylesheet" href="https://fonts.googleapis.com/css2?family=Arimo:wght@400;600;700&display=swap">
<style>
  :root {
    --bg: #2e2f33;
    --card-grey: #6d6e71;
    --card-grey-light: #d6d7da;
    --white: #ffffff;
    --brand-blue: #1c3fae;
    --ink: #1e1f22;
    --icon-dark: #2a2a2c;
    --sky-top: #3f6fb8;
    --sky-mid: #9fbbe0;
    --sky-cloud: #e9eef5;
  }
  * { box-sizing: border-box; margin: 0; padding: 0; }
  html, body { width: 1200px; height: 800px; overflow: hidden; }
  body {
    background: var(--bg);
    font-family: "Arimo", Arial, sans-serif;
    display: flex;
    align-items: center;
    justify-content: center;
    gap: 40px;
  }
  .card {
    position: relative;
    width: 560px;
    height: 320px;
    background: var(--card-grey);
    overflow: hidden;
    box-shadow: 0 6px 18px rgba(0,0,0,.35);
  }
  .card-shapes { position: absolute; inset: 0; }

  /* front */
  .brand {
    position: absolute;
    left: 0; right: 0; top: 128px;
    display: flex;
    align-items: center;
    justify-content: center;
    gap: 14px;
  }
  .brand-mark {
    width: 52px; height: 52px;
    background: var(--brand-blue);
  }
  .brand-name {
    color: var(--brand-blue);
    font-weight: 700;
    font-size: 34px;
    letter-spacing: 1px;
  }

  /* back */
  .contact {
    position: absolute;
    left: 26px; top: 44px;
    color: var(--ink);
    font-size: 14px;
    line-height: 1.3;
  }
  .contact-row { display: flex; align-items: flex-start; gap: 14px; margin-bottom: 20px; }
  .contact-icon {
    flex: none;
    width: 34px; height: 34px;
    border-radius: 50%;
    background: var(--icon-dark);
    display: flex; align-items: center; justify-content: center;
  }
  .contact-text { padding-top: 2px; white-space: nowrap; }
  .holder {
    position: absolute;
    right: 18px; top: 50px;
    text-align: right;
    white-space: nowrap;
  }
  .holder-name { color: var(--ink); font-size: 20px; font-weight: 400; }
  .holder-title { color: var(--white); font-size: 14px; margin-top: 5px; }
</style>
</head>
<body>

  <!-- front side -->
  <section class="card card-front">
    <svg class="card-shapes" width="560" height="320" viewBox="0 0 560 320" aria-hidden="true">
      <rect x="0" y="56" width="560" height="14" fill="var(--card-grey-light)"/>
      <rect x="0" y="70" width="560" height="180" fill="var(--white)"/>
      <rect x="0" y="250" width="560" height="14" fill="var(--card-grey-light)"/>
      <g fill="var(--brand-blue)">
        <polygon points="0,10 196,10 204,15 196,20 0,20"/>
        <polygon points="0,24 206,24 214,29 206,34 0,34"/>
        <polygon points="0,38 216,38 224,43 216,48 0,48"/>
        <polygon points="230,38 240,38 248,43 240,48 230,48 238,43"/>
        <polygon points="560,272 364,272 356,277 364,282 560,282"/>
        <polygon points="560,286 354,286 346,291 354,296 560,296"/>
        <polygon points="560,300 344,300 336,305 344,310 560,310"/>
        <polygon points="330,272 320,272 312,277 320,282 330,282 322,277"/>
      </g>
    </svg>
    <div class="brand">
      <span class="brand-mark"></span>
      <span class="brand-name">Veltra Aviation</span>
    </div>
  </section>

  <!-- back side -->
  <section class="card card-back">
    <svg class="card-shapes" width="560" height="320" viewBox="0 0 560 320">
      <defs>
        <linearGradient id="sky" x1="0" y1="0" x2="0" y2="1">
          <stop offset="0" stop-color="var(--sky-top)"/>
          <stop offset=".55" stop-color="var(--sky-mid)"/>
          <stop offset="1" stop-color="var(--sky-cloud)"/>
        </linearGradient>
      </defs>
      <rect class="aircraft-photo" role="img" aria-label="Photo of an airliner flying head-on above clouds"
            x="250" y="112" width="310" height="168" fill="url(#sky)"/>
      <polygon points="0,0 290,0 262,286 0,238" fill="var(--white)"/>
    </svg>

    <div class="contact">
      <div class="contact-row">
        <span class="contact-icon">
          <svg width="16" height="18" viewBox="0 0 16 18" aria-hidden="true">
            <path d="M8 1a6 6 0 0 0-6 6c0 4.5 6 10 6 10s6-5.5 6-10a6 6 0 0 0-6-6z" fill="#fff"/>
            <circle cx="8" cy="7" r="2.2" fill="var(--icon-dark)"/>
          </svg>
        </span>
        <div class="contact-text">482 Pellow St.<br>Halvick , OR<br>08519</div>
      </div>
      <div class="contact-row">
        <span class="contact-icon">
          <svg width="18" height="14" viewBox="0 0 18 14" aria-hidden="true">
            <rect x="1" y="1" width="16" height="12" fill="none" stroke="#fff" stroke-width="1.6"/>
            <polyline points="1,1 9,8 17,1" fill="none" stroke="#fff" stroke-width="1.6"/>
          </svg>
        </span>
        <div class="contact-text">Lwskyfixtech@mailvora.com</div>
      </div>
    </div>

    <div class="holder">
      <div class="holder-name">Tiberio Malvade Furtunato</div>
      <div class="holder-title">Aircraft Maintenance Manager</div>
    </div>
  </section>

</body>
</html>
```